web design for specialty coffee shop

We are online shop selling specialty coffeee.
Our brand concept keywords are -
specialty coffee, knowledge, discovery, professional, convenience, collaboration.
there will be five main tabs on the homepage
[home (u icon from logo)]
[coffee]
[equipment]
[gift]
[knowledge]
[about us]
For our site, we will be using the following template.
ONLY DESIGN, NO CODING necessary as our developers will do that.
http://plendrixthemes.net/item/velmora-premium-responsive-shopcart-theme/full_screen_preview/7302514
Use the template as a base.
You do not have to do exactly the same layout.
Creative Liberty!
For the style and color palette, please look at the attached image.
Our brown logo should match nicely with the style provided in the attachment.
Thank you for taking the time to read this post.
Looking forward to working with artquivery and the amazing designers that are part of this community.
Reason: Dear designers,
I have extended the deadline to give designers who accepted to participate in this contest some more time to submit their designs. Thank you for understanding.
Coffee Shop

```html
<!DOCTYPE html>
<html lang="en">
<head>
<meta charset="utf-8">
<title>Marrowby Coffee Lab</title>
<link rel="stylesheet" href="https://fonts.googleapis.com/css2?family=Ultra&family=Oswald:wght@400&family=Arimo:wght@400;700&display=swap">
<style>
  :root{
    --teal:#4fb3b8;
    --teal-text:#45aab3;
    --cream:#f8ebcd;
    --cream-light:#fcf3de;
    --espresso:#2a0000;
    --brown:#7a4a1e;
    --brown-dark:#2b0a05;
    --title-brown:#8b4a12;
    --rust:#e4502a;
    --black:#050505;
    --white:#ffffff;
  }
  *{margin:0;padding:0;box-sizing:border-box}
  html,body{width:1200px;height:1165px;overflow:hidden}
  body{position:relative;font-family:"Arimo",Arial,sans-serif;background:var(--cream)}

  .topbar{position:absolute;left:0;top:0;width:1200px;height:40px;background:var(--teal)}
  .account-links{position:absolute;right:252px;top:0;height:40px;display:flex;align-items:center;font-size:10px;color:var(--white)}
  .account-links span{padding:0 12px;line-height:32px;border-left:1px solid rgba(255,255,255,.35)}
  .account-links span:first-child{border-left:none}

  .header{position:absolute;left:0;top:40px;width:1200px;height:112px;background:radial-gradient(ellipse at center,var(--cream-light),var(--cream))}
  .search{position:absolute;left:216px;top:36px;width:170px;height:30px;background:var(--white);font-size:9.5px;color:#666;padding:9px 7px}
  .search svg{position:absolute;right:7px;top:7px}
  .brand{position:absolute;left:450px;top:18px;width:300px;text-align:center;color:var(--brown-dark);font-weight:700}
  .brand-name{font-size:50px;line-height:56px;letter-spacing:-1px}
  .brand-sub{font-size:18px;letter-spacing:6px;line-height:20px}

  .mainnav{position:absolute;left:0;top:152px;width:1200px;height:44px;background:var(--espresso);display:flex;justify-content:center;align-items:center;gap:16px;color:var(--white);font-weight:700;font-size:11.5px;padding-left:10px}

  .hero{position:absolute;left:0;top:196px;width:1200px;height:384px;background:radial-gradient(ellipse 45% 70% at 35% 55%,#e5a985 0%,#c97d50 35%,#8f4f22 70%,#6a3a18 100%)}
  .hero-copy{position:absolute;right:232px;top:72px;text-align:right}
  .hero-title{font-family:"Ultra",Georgia,serif;font-size:23px;color:var(--white);letter-spacing:.5px;white-space:nowrap}
  .hero-sub{font-family:"Oswald",sans-serif;font-size:21px;color:var(--teal);margin-top:4px;letter-spacing:-.5px}
  .hero-text{font-family:"Oswald",sans-serif;font-size:12px;line-height:14.4px;color:var(--teal);margin-top:9px;width:134px;margin-left:auto;text-transform:uppercase;letter-spacing:-.4px}
  .slide-arrow{position:absolute;top:144px}
  .slide-arrow.prev{left:15px}
  .slide-arrow.next{right:10px}
  .slide-dots{position:absolute;left:891px;top:363px;display:flex;gap:4px}
  .slide-dots i{width:8px;height:8px;border-radius:50%;background:var(--white)}
  .slide-dots i.active{background:var(--teal)}

  .features{position:absolute;left:0;top:580px;width:1200px;height:268px;background:radial-gradient(ellipse at center,var(--cream-light),var(--cream))}
  .card{position:absolute;top:54px;width:253px;height:168px}
  .card-title{position:absolute;left:0;width:100%;top:86px;text-align:center;font-weight:700;font-size:17.5px;color:var(--white)}
  .card-title.rust{color:var(--rust)}
  .card-title.stacked{text-align:left;left:12px;top:16px;line-height:19px}
  .card-btn{position:absolute;left:81px;top:114px;width:90px;height:30px;border:1px solid #333;background:rgba(255,255,255,.75);font-size:10px;text-align:center;line-height:28px;color:#111}
  .card-btn.dark{background:rgba(60,60,60,.7);color:var(--white);border-color:#ddd}

  .how{position:absolute;left:0;top:848px;width:1200px;height:262px;background:var(--white)}
  .how-heading{position:absolute;left:537px;top:28px;display:flex;align-items:center;gap:8px}
  .how-title{font-family:"Ultra",Georgia,serif;font-size:16px;color:var(--title-brown);white-space:nowrap}
  .step{position:absolute;top:84px;width:160px;text-align:center}
  .step-illustration{width:80px;height:80px;margin:0 auto;border-radius:6px;background:linear-gradient(160deg,#9a6230,var(--brown))}
  .step-label{font-family:"Oswald",sans-serif;font-size:11.5px;line-height:13px;color:var(--teal-text);text-transform:uppercase;letter-spacing:-.3px;margin-top:8px}

  .footer{position:absolute;left:0;top:1110px;width:1200px;height:55px;background:var(--black)}
  .copyright{position:absolute;left:0;width:1216px;top:27px;text-align:center;font-size:10px;color:#aaa}
  .social{position:absolute;left:896px;top:14px;width:30px;height:30px;background:#555;border-radius:3px}
</style>
</head>
<body>
  <div class="topbar">
    <nav class="account-links"><span>Sign in</span><span>Register</span><span>Cart (0)</span></nav>
  </div>

  <header class="header">
    <div class="search">search entire store here
      <svg width="16" height="16" viewBox="0 0 16 16"><circle cx="10" cy="6" r="4.5" fill="none" stroke="#777" stroke-width="1.5"/><line x1="6.8" y1="9.2" x2="2" y2="14" stroke="#777" stroke-width="2"/></svg>
    </div>
    <div class="brand">
      <div class="brand-name">marrowby</div>
      <div class="brand-sub">coffee lab</div>
    </div>
  </header>

  <nav class="mainnav"><span>COFFEE</span><span>EQUIPMENT</span><span>GIFT</span><span>KNOWLEDGE</span><span>ABOUT US</span></nav>

  <section class="hero" role="img" aria-label="Photo of a woman sipping from a white coffee cup">
    <svg class="slide-arrow prev" width="30" height="38" viewBox="0 0 30 38"><polygon points="27,3 3,19 27,35" fill="none" stroke="#9a9a9a" stroke-width="5"/></svg>
    <svg class="slide-arrow next" width="30" height="38" viewBox="0 0 30 38"><polygon points="3,3 27,19 3,35" fill="none" stroke="#9a9a9a" stroke-width="5"/></svg>
    <div class="hero-copy">
      <div class="hero-title">CHOOSE YOUR TASTE !</div>
      <div class="hero-sub">IN 3 EASY STEPS</div>
      <p class="hero-text">Lorem ipsum dolor sit amet, consectetuer adipiscing elit. Nam cursus. Morbi ut mi. Nullam enim leo, egestas id, condimentum at, laoreet mattis, massa. Sed eleifend</p>
    </div>
    <div class="slide-dots"><i></i><i></i><i></i><i class="active"></i><i></i></div>
  </section>

  <section class="features">
    <div class="card" style="left:208px;background:linear-gradient(135deg,#f3ddd0,#d7a68c 45%,#5a3420 75%,#3a2214)" role="img" aria-label="Photo of roasted coffee beans held in a hand">
      <div class="card-title">LOREM IPUSM DOLOR SIT</div>
      <div class="card-btn">view</div>
    </div>
    <div class="card" style="left:472px;background:linear-gradient(160deg,#555,#d8d8d8 40%,#f3f1ee 60%,#777)" role="img" aria-label="Photo of a cappuccino in a white cup">
      <div class="card-title rust">LOREM IPUSM DOLOR SIT</div>
      <div class="card-btn dark">view</div>
    </div>
    <div class="card" style="left:736px;background:linear-gradient(160deg,#fbf0dc,#ead3b6 40%,#a45a2c 75%,#6a2e12)" role="img" aria-label="Photo of coffee beans spilling from a scoop">
      <div class="card-title rust stacked">LOREM<br>IPUSM<br>DOLOR SIT</div>
      <div class="card-btn">view</div>
    </div>
  </section>

  <section class="how">
    <div class="how-heading">
      <div class="how-title">HOW IT WORKS !</div>
      <svg width="24" height="20" viewBox="0 0 24 20"><path d="M2 6 Q12 0 18 12" fill="none" stroke="#4fb3b8" stroke-width="3" stroke-linecap="round"/><path d="M12 14 L19 16 L20 8" fill="none" stroke="#4fb3b8" stroke-width="3" stroke-linecap="round"/></svg>
    </div>

    <div class="step" style="left:242px">
      <div class="step-illustration" role="img" aria-label="Illustration of a coffee mug with a dollar sign"></div>
      <div class="step-label">Choose your<br>subscription</div>
    </div>
    <div class="step" style="left:414px">
      <div class="step-illustration" role="img" aria-label="Illustration of an open cardboard box"></div>
      <div class="step-label">Your marrowby<br>box delivered</div>
    </div>
    <div class="step" style="left:586px">
      <div class="step-illustration" role="img" aria-label="Illustration of three coffee beans"></div>
      <div class="step-label">Brew 4 coffees<br>and pick a favourite</div>
    </div>
    <div class="step" style="left:772px">
      <div class="step-illustration" role="img" aria-label="Illustration of a coffee shopping bag"></div>
      <div class="step-label">Get a full bag<br>with free shipping</div>
    </div>
  </section>

  <footer class="footer">
    <div class="copyright">© copyright Marrowby Coffee Lab 2013. All rights reserved</div>
    <div class="social"></div>
  </footer>
</body>
</html>
```